The Queen Rides Again Line of Sparkling Wine & Spirits

Back info: Tara Joy Whitfield Owner 209-555-0143 1700 E. Harlowe Rd, Bldg. 2, & 3, Calder Ca. 95111
Sparkling Wines & Keepsakes www.thequeenridesagain.example
Ok I have uploaded the winning design. The color that I am after is the Fushia, Raspberry, Red, Matte Satin Matalic Finish. With a 24 Karet Gold color Foil. The Bottle is on the top row and it's the 2nd Bottle in. That is the Color that I want. This is the style of font. Make sure that you put what we're advertising. Good Luck to you all. Warmest regards, Tara
Target Market(s)
21 & up UniSex
Industry/Entity Type
Sparkling Wine and Memorabilia
Contact Information for Business Card
there listed up above.....
Look and feel

```html
<!DOCTYPE html>
<html lang="en">
<head>
<meta charset="utf-8">
<title>The Queen Rides Again – Business Card</title>
<link rel="stylesheet" href="https://fonts.googleapis.com/css2?family=Cinzel:wght@400;600&display=swap">
<style>
  :root {
    --backdrop: #3a3a3c;
    --magenta: #dc1388;
    --magenta-deep: #8c0f4c;
    --raspberry: #b3125f;
    --gold: #d2a93e;
    --ink: #1c1c1c;
    --paper-white: #ffffff;
  }
  * { box-sizing: border-box; margin: 0; padding: 0; }
  html, body {
    width: 1200px; height: 1200px; overflow: hidden;
    background: var(--backdrop);
    font-family: "Cinzel", "Times New Roman", serif;
  }
  .canvas { position: relative; width: 1200px; height: 1200px; }
  .card {
    position: absolute; left: 180px;
    width: 840px; height: 480px;
    border-radius: 36px;
    border: 3px solid var(--gold);
    overflow: hidden;
    background: linear-gradient(115deg, var(--raspberry) 0%, var(--magenta) 40%, var(--magenta) 60%, var(--magenta-deep) 100%);
  }
  .card--front { top: 90px; }
  .card--back { top: 630px; }

  .contact { position: absolute; left: 60px; top: 70px; }
  .contact__name {
    color: var(--gold); font-size: 38px; font-weight: 600; line-height: 1;
    text-transform: uppercase; letter-spacing: 1px;
  }
  .contact__role {
    color: var(--paper-white); font-size: 24px; font-weight: 400; line-height: 1.2; margin-top: 6px;
    text-transform: uppercase;
  }
  .contact__list { list-style: none; margin-top: 16px; }
  .contact__item {
    display: flex; align-items: center; gap: 12px;
    color: var(--paper-white); font-size: 16px; font-weight: 400; line-height: 26px;
    text-transform: uppercase; white-space: nowrap;
  }
  .contact__item--indent { padding-left: 32px; }
  .contact__icon { width: 20px; height: 20px; flex: none; }

  .brand-mark {
    position: absolute; right: 50px; top: 90px; width: 260px;
    text-align: center; color: var(--gold);
    font-size: 32px; font-weight: 600; line-height: 1.15;
    text-transform: uppercase;
  }

  .gold-rule {
    position: absolute; left: 0; right: 0; top: 330px; height: 12px;
    background: var(--gold);
  }
  .pattern-band {
    position: absolute; left: 0; right: 0; top: 342px; bottom: 0;
    background: linear-gradient(90deg, #4a1030 0%, #6a1242 50%, #4a1030 100%);
  }

  .back-mark {
    position: absolute; inset: 0;
    display: flex; align-items: center; justify-content: center;
    color: var(--ink); font-size: 44px; font-weight: 600;
    text-transform: uppercase;
  }
</style>
</head>
<body>
<main class="canvas">

  <section class="card card--front">
    <div class="contact">
      <h1 class="contact__name">Tara Joy Whitfield</h1>
      <p class="contact__role">Owner</p>
      <ul class="contact__list">
        <li class="contact__item">
          <svg class="contact__icon" viewBox="0 0 24 24" aria-hidden="true"><path fill="#d2a93e" d="M6.6 10.8a15.1 15.1 0 0 0 6.6 6.6l2.2-2.2c.3-.3.7-.4 1-.2 1.1.4 2.3.6 3.6.6.6 0 1 .4 1 1V20c0 .6-.4 1-1 1A17 17 0 0 1 3 4c0-.6.4-1 1-1h3.5c.6 0 1 .4 1 1 0 1.3.2 2.5.6 3.6.1.3 0 .7-.2 1z"/></svg>
          209-555-0143
        </li>
        <li class="contact__item">
          <svg class="contact__icon" viewBox="0 0 24 24" aria-hidden="true"><g fill="none" stroke="#d2a93e" stroke-width="1.8"><circle cx="12" cy="12" r="9"/><ellipse cx="12" cy="12" rx="4" ry="9"/><path d="M3 12h18M4.5 7.5h15M4.5 16.5h15"/></g></svg>
          www.thequeenridesagain.example
        </li>
        <li class="contact__item">
          <svg class="contact__icon" viewBox="0 0 24 24" aria-hidden="true"><path fill="none" stroke="#d2a93e" stroke-width="2" d="M12 22s7-7.2 7-12.5A7 7 0 0 0 5 9.5C5 14.8 12 22 12 22z"/><circle cx="12" cy="9.5" r="2.5" fill="#d2a93e"/></svg>
          1700 E. Harlowe Rd, Bldg. 2, &amp; 3,
        </li>
        <li class="contact__item contact__item--indent">Calder Ca. 95111</li>
        <li class="contact__item contact__item--indent">Sparkling Wines &amp; Keepsakes</li>
      </ul>
    </div>

    <div class="brand-mark">The Queen<br>Rides Again</div>

    <div class="gold-rule"></div>
    <div class="pattern-band" role="img" aria-label="Decorative black lattice pattern on raspberry ground"></div>
  </section>

  <section class="card card--back">
    <div class="back-mark">The Queen Rides Again</div>
  </section>

</main>
</body>
</html>
```